Business Card for Pottery and Jewellery Designer

A new business card design is needed to accompany a newly launching pottery and jewellery website. The company logo has been attached for use. The company is called Kilnwick Lane. For a sense of the vibe please see the website (it is currently under construction but this way you'll get a feel for the style) www.KilnwickLane.com

The website font is Pontano Sans for the body of the text with Overlock for headers.

The overall look should be clean and elegant. The back side can have just the logo. The front side should have a smaller logo and the following details displayed:

Kilnwick Lane
Designer: Marisol Bexley
Phone: xxx.xxx.xxxx
Email: Designer@KilnwickLane.com

The structure of displaying this is completely up to you. Different layouts and creative methods of displaying contact info are welcome as long as it stays clean/uncluttered.

No product photographs are to be included in the design as the catalogue changes quickly.

Colour preferences lean towards elegant and understated (charcoal grey, dark navy blue etc.)

Please let me know if you have any further questions or further details required.

Target Market(s)

Target market is 30+ year old women

Industry/Entity Type

Construction

Colors
ffffff
1b1b1b
474747
d9d9d9
fafafa
0355a3

Requirements
Must have
• The submissions so far have looked very typical and don't stand out right now. They're also all in navy with very little variation. I'm looking for something that stands out a it more while still being clean-looking.
Nice to have
• I've attached a few design samples and an idea for a backdrop. It would be great to see some designs in black, white, and grey with only a hint of color.
Should not have
• Product Images

```html
<!DOCTYPE html>
<html lang="en">
<head>
<meta charset="utf-8">
<title>Kilnwick Lane — Business Card</title>
<link rel="stylesheet" href="https://fonts.googleapis.com/css2?family=Overlock:wght@400;700&family=Pontano+Sans&family=Lato:wght@400&display=swap">
<style>
  :root {
    --sheet-bg: #ffffff;
    --navy: #27225f;
    --navy-text: #2e2a6e;
    --ink-grey: #5a5a5a;
    --rule-grey: #8c8c8c;
    --icon-grey: #9a9a9a;
    --ghost-grey: #f1f1f2;
    --card-border: #7a7a7a;
    --label: #1b1b1b;
    --white: #ffffff;
  }
  * { margin: 0; padding: 0; box-sizing: border-box; }
  html, body {
    width: 784px; height: 1200px; overflow: hidden;
    background: var(--sheet-bg);
  }
  .sheet { position: relative; width: 784px; height: 1200px; }

  .side-label {
    position: absolute; left: 45px;
    font: 13px "Lato", sans-serif; color: var(--label);
  }
  .side-label--front { top: 53px; }
  .side-label--back { top: 640px; }

  .card {
    position: absolute; left: 25px; width: 731px; height: 413px;
    overflow: hidden;
  }
  .card--front {
    top: 120px; background: var(--white);
    border: 1px solid var(--card-border);
  }
  .card--back { top: 695px; background: var(--navy); }

  .ghost-mark {
    position: absolute; left: 330px; top: 180px;
    width: 460px; height: 460px; border-radius: 50%;
    background: var(--ghost-grey);
  }

  .front-brand {
    position: absolute; left: 40px; top: 60px; width: 190px;
    text-align: center; color: var(--navy);
  }
  .brand-dot {
    display: block; margin: 0 auto 10px;
    width: 62px; height: 62px; border-radius: 50%;
    background: var(--navy);
  }
  .brand-name {
    font-family: "Overlock", sans-serif; font-weight: 400;
    letter-spacing: 1px; line-height: 1.02;
  }
  .front-brand .brand-name { font-size: 31px; }

  .divider {
    position: absolute; left: 265px; top: 55px;
    width: 1px; height: 157px; background: var(--rule-grey);
  }

  .contact { position: absolute; left: 293px; top: 56px; }
  .contact__name {
    font: 400 24px "Overlock", sans-serif; color: var(--navy-text);
    text-transform: uppercase; letter-spacing: 0.5px; line-height: 1;
  }
  .contact__role {
    margin-top: 5px;
    font: 15px "Pontano Sans", sans-serif; color: var(--navy-text);
  }
  .contact__lines {
    margin-top: 12px; list-style: none;
    font: 20px "Pontano Sans", sans-serif; color: var(--ink-grey); line-height: 1.2;
  }
  .social { display: flex; gap: 16px; margin-top: 16px; list-style: none; }
  .social__item {
    width: 23px; height: 23px; border-radius: 50%; background: var(--icon-grey);
  }

  .back-seal {
    position: absolute; left: 205px; top: 22px;
    width: 326px; height: 314px; border-radius: 50%;
    background: var(--white);
    display: flex; flex-direction: column; align-items: center; justify-content: center;
    color: var(--navy);
  }
  .back-seal .brand-dot { width: 80px; height: 80px; margin-bottom: 14px; }
  .back-seal .brand-name { font-size: 42px; text-align: center; }

  .back-url {
    position: absolute; left: 0; right: 0; top: 356px;
    text-align: center;
    font: 400 25px "Overlock", sans-serif; color: var(--white); letter-spacing: 0.3px;
  }
</style>
</head>
<body>
<main class="sheet">
  <p class="side-label side-label--front">Front</p>
  <section class="card card--front" aria-label="Business card front">
    <div class="ghost-mark" aria-hidden="true"></div>
    <div class="front-brand">
      <span class="brand-dot" aria-hidden="true"></span>
      <p class="brand-name">Kilnwick<br>Lane</p>
    </div>
    <div class="divider" aria-hidden="true"></div>
    <div class="contact">
      <p class="contact__name">Marisol Bexley</p>
      <p class="contact__role">Designer</p>
      <ul class="contact__lines">
        <li>000.000.0000</li>
        <li>Designer@KilnwickLane.com</li>
      </ul>
      <ul class="social" aria-label="Social profiles">
        <li class="social__item"></li>
        <li class="social__item"></li>
        <li class="social__item"></li>
        <li class="social__item"></li>
      </ul>
    </div>
  </section>

  <p class="side-label side-label--back">Back</p>
  <section class="card card--back" aria-label="Business card back">
    <div class="back-seal">
      <span class="brand-dot" aria-hidden="true"></span>
      <p class="brand-name">Kilnwick<br>Lane</p>
    </div>
    <p class="back-url">www.KilnwickLane.com</p>
  </section>
</main>
</body>
</html>
```